Olive Oil Label Needs Graphic Designs

We need two sister label designs for 500ml bottles for our new brand "Casa Lumen". Casa Lumen is a high-end olive oil from Baeza, Spain which will be sold in the US. The oil will be produced from both Arbequina olives and Picual olives. Therefore, envisioning the same design just a different color scheme for the different labels.
The label should have the following characteristics; clean and simple, stand-out from mainstream labels, be eye-catching, give perception of high-end / high-quality.
Our current thinking of what we want (but please let your creative juices flow); lighter background, to be more eye catching, graphics of and olive, a olive branch or olive tree.
Text which should appear on the label are (not necessarily in this order);
Casa Lumen
Extra Virgin Olive Oil
Family Reserve
Arbequina (One design)
Picual (Second design)
The label should be about 3 inches wide and 5.5 inches in height.

```html
<!DOCTYPE html>
<html lang="en">
<head>
<meta charset="utf-8">
<title>Casa Lumen – Extra Virgin Olive Oil Labels</title>
<link rel="stylesheet" href="https://fonts.googleapis.com/css2?family=Mulish:wght@400;600&family=Kaushan+Script&family=Marcellus&display=swap">
<style>
  :root {
    --page: #ffffff;
    --label-black: #050806;
    --frame-light: #e8ecb0;
    --frame-mid: #a6b94a;
    --frame-dark: #4a5d1c;
    --olive-leaf: #8cbd3a;
    --olive-deep: #3f6a1e;
    --swoosh: #2d3f1a;
    --dot-gold: #8a7a3a;
    --ribbon: #1f3d25;
    --ribbon-edge: #c9d98a;
    --text-light: #ffffff;
    --text-cream: #e9ecd2;
  }
  html, body {
    margin: 0;
    width: 1200px;
    height: 900px;
    overflow: hidden;
    background: var(--page);
  }
  .canvas {
    position: relative;
    width: 1200px;
    height: 900px;
  }
  .label {
    position: absolute;
    top: 118px;
    width: 360px;
    height: 665px;
    overflow: hidden;
  }
  .label--arbequina { left: 200px; }
  .label--picual { left: 640px; }

  .stop-frame-light { stop-color: var(--frame-light); }
  .stop-frame-mid { stop-color: var(--frame-mid); }
  .stop-frame-dark { stop-color: var(--frame-dark); }
  .stop-black { stop-color: var(--label-black); stop-opacity: 0; }
  .stop-dots { stop-color: var(--dot-gold); stop-opacity: 0.5; }
  .stop-leaf { stop-color: var(--olive-leaf); }
  .stop-leaf-fade { stop-color: var(--olive-deep); stop-opacity: 0; }

  .label-field { fill: var(--label-black); }
  .swoosh { fill: var(--swoosh); }
  .ribbon { fill: var(--ribbon); stroke: var(--ribbon-edge); stroke-width: 3; }

  .brand-name {
    font-family: "Mulish", sans-serif;
    font-weight: 600;
    font-size: 48px;
    fill: var(--text-light);
  }
  .product-type {
    font-family: "Mulish", sans-serif;
    font-weight: 400;
    font-size: 21px;
    fill: var(--text-light);
  }
  .variety {
    font-family: "Kaushan Script", cursive;
    font-size: 31px;
    fill: var(--text-light);
    letter-spacing: 1px;
  }
  .reserve {
    font-family: "Marcellus", serif;
    font-size: 18px;
    fill: var(--text-cream);
    letter-spacing: 0.5px;
  }
</style>
</head>
<body>
<main class="canvas">

  <svg class="label label--arbequina" viewBox="0 0 360 665" aria-label="Casa Lumen Arbequina label">
    <defs>
      <linearGradient id="frameA" x1="0" y1="0" x2="1" y2="1">
        <stop offset="0" class="stop-frame-light"/>
        <stop offset="0.45" class="stop-frame-mid"/>
        <stop offset="1" class="stop-frame-dark"/>
      </linearGradient>
      <radialGradient id="dotsA" cx="0.55" cy="0.35" r="0.6">
        <stop offset="0" class="stop-black"/>
        <stop offset="0.5" class="stop-dots"/>
        <stop offset="1" class="stop-black"/>
      </radialGradient>
      <radialGradient id="treeA" cx="0.5" cy="0.4" r="0.55">
        <stop offset="0" class="stop-leaf"/>
        <stop offset="1" class="stop-leaf-fade"/>
      </radialGradient>
      <clipPath id="fieldA">
        <path d="M14,155 Q14,16 180,16 Q346,16 346,155 V510 Q346,649 180,649 Q14,649 14,510 Z"/>
      </clipPath>
    </defs>
    <path class="label-frame" fill="url(#frameA)" d="M0,150 Q0,0 180,0 Q360,0 360,150 V515 Q360,665 180,665 Q0,665 0,515 Z"/>
    <path class="label-field" d="M14,155 Q14,16 180,16 Q346,16 346,155 V510 Q346,649 180,649 Q14,649 14,510 Z"/>
    <g clip-path="url(#fieldA)">
      <rect role="img" aria-label="Swirling halftone dot pattern" x="14" y="16" width="332" height="480" fill="url(#dotsA)"/>
      <path class="swoosh" d="M10,280 Q40,490 360,425 L360,452 Q40,530 10,330 Z"/>
      <ellipse role="img" aria-label="Olive tree emblem with leafy branches" cx="180" cy="155" rx="95" ry="110" fill="url(#treeA)"/>
    </g>
    <text class="brand-name" x="180" y="335" text-anchor="middle">Casa Lumen</text>
    <text class="product-type" x="180" y="416" text-anchor="middle">Extra Virgin Olive Oil</text>
    <text class="variety" x="180" y="492" text-anchor="middle">Arbequina</text>
    <path class="ribbon" d="M48,560 Q180,545 312,560 L304,606 Q180,592 56,606 Z"/>
    <text class="reserve" x="180" y="586" text-anchor="middle">FAMILY RESERVE</text>
  </svg>

  <svg class="label label--picual" viewBox="0 0 360 665" aria-label="Casa Lumen Picual label">
    <defs>
      <linearGradient id="frameP" x1="0" y1="0" x2="1" y2="1">
        <stop offset="0" class="stop-frame-light"/>
        <stop offset="0.45" class="stop-frame-mid"/>
        <stop offset="1" class="stop-frame-dark"/>
      </linearGradient>
      <radialGradient id="dotsP" cx="0.55" cy="0.35" r="0.6">
        <stop offset="0" class="stop-black"/>
        <stop offset="0.5" class="stop-dots"/>
        <stop offset="1" class="stop-black"/>
      </radialGradient>
      <radialGradient id="treeP" cx="0.5" cy="0.4" r="0.55">
        <stop offset="0" class="stop-leaf"/>
        <stop offset="1" class="stop-leaf-fade"/>
      </radialGradient>
      <clipPath id="fieldP">
        <path d="M14,155 Q14,16 180,16 Q346,16 346,155 V510 Q346,649 180,649 Q14,649 14,510 Z"/>
      </clipPath>
    </defs>
    <path class="label-frame" fill="url(#frameP)" d="M0,150 Q0,0 180,0 Q360,0 360,150 V515 Q360,665 180,665 Q0,665 0,515 Z"/>
    <path class="label-field" d="M14,155 Q14,16 180,16 Q346,16 346,155 V510 Q346,649 180,649 Q14,649 14,510 Z"/>
    <g clip-path="url(#fieldP)">
      <rect role="img" aria-label="Swirling halftone dot pattern" x="14" y="16" width="332" height="480" fill="url(#dotsP)"/>
      <path class="swoosh" d="M10,280 Q40,490 360,425 L360,452 Q40,530 10,330 Z"/>
      <ellipse role="img" aria-label="Olive tree emblem with leafy branches" cx="180" cy="155" rx="95" ry="110" fill="url(#treeP)"/>
    </g>
    <text class="brand-name" x="180" y="335" text-anchor="middle">Casa Lumen</text>
    <text class="product-type" x="180" y="416" text-anchor="middle">Extra Virgin Olive Oil</text>
    <text class="variety" x="180" y="492" text-anchor="middle">Picual</text>
    <path class="ribbon" d="M48,560 Q180,545 312,560 L304,606 Q180,592 56,606 Z"/>
    <text class="reserve" x="180" y="586" text-anchor="middle">FAMILY RESERVE</text>
  </svg>

</main>
</body>
</html>
```